Mortgage Broker Site

Need a custom design for a mortgage broker site - please refer to the attached Word .doc that gives more detail.

Number of Pages Required

5+ page

Colors

Designer to choose colors to be used in the design.

```html
<!DOCTYPE html>
<html lang="en">
<head>
<meta charset="utf-8">
<title>Homevale – Mortgage Calculators</title>
<link href="https://fonts.googleapis.com/css2?family=Poppins:wght@500;700&family=Roboto:wght@400;500&display=swap" rel="stylesheet">
<style>
  :root {
    --red: #bf0202;
    --ice: #edf4ff;
    --blue: #1856a6;
    --ink: #333333;
    --text: #3d3d3d;
    --white: #ffffff;
    --stage: #f2f2f2;
    --band: #3b3836;
    --gold: #f2a516;
  }
  * { margin: 0; padding: 0; box-sizing: border-box; }
  html, body { width: 1200px; height: 2280px; overflow: hidden; background: var(--stage); }
  body { position: relative; font-family: "Roboto", sans-serif; color: var(--text); }

  .page { position: absolute; left: 0; top: 484px; width: 1200px; height: 1311px; box-shadow: 0 4px 24px rgba(0,0,0,.08); }
  .abs { position: absolute; }

  /* header */
  .site-header { position: absolute; left: 0; top: 0; width: 1200px; height: 53px; background: var(--white); }
  .brand { position: absolute; font-family: "Poppins", sans-serif; font-weight: 500; display: flex; align-items: center; gap: 6px; }
  .brand-mark { width: 9px; height: 9px; background: var(--red); }
  .site-header .brand { left: 173px; top: 12px; font-size: 25px; color: var(--ink); line-height: 30px; }
  .nav-link { position: absolute; top: 0; line-height: 53px; font-size: 12px; font-weight: 500; color: var(--ink); }
  .btn { position: absolute; background: var(--red); color: var(--white); font-size: 10px; font-weight: 500; letter-spacing: 2px; text-transform: uppercase; display: flex; align-items: center; justify-content: center; }
  .btn-apply { left: 917px; top: 10px; width: 110px; height: 34px; font-size: 9.5px; }

  /* tools */
  .tools { position: absolute; left: 0; top: 53px; width: 1200px; height: 494px; background: var(--ice); }
  .eyebrow { position: absolute; left: 0; width: 1200px; top: 60px; text-align: center; color: var(--red); font-size: 8.5px; letter-spacing: 2.4px; text-transform: uppercase; }
  .section-title { position: absolute; left: 0; width: 1200px; text-align: center; font-family: "Poppins", sans-serif; font-weight: 700; color: var(--ink); }
  .tools .section-title { top: 78px; font-size: 21px; }
  .tool { position: absolute; width: 240px; margin-left: -120px; text-align: center; }
  .tool svg { display: block; margin: 0 auto; width: 46px; height: 46px; }
  .tool-name { margin-top: 20px; font-family: "Poppins", sans-serif; font-weight: 500; font-size: 13.5px; color: var(--ink); }
  .tool-desc { margin-top: 6px; font-size: 10.3px; line-height: 17.5px; color: var(--text); }

  /* quote band */
  .quote { position: absolute; left: 0; top: 547px; width: 1200px; height: 214px; background: linear-gradient(100deg, #423f3c, #363433 55%, #3e3a38); }
  .quote .section-title { top: 44px; font-size: 21px; color: var(--white); }
  .btn-purchase { left: 437px; top: 123px; width: 144px; height: 40px; font-size: 9px; }
  .btn-refi { left: 619px; top: 123px; width: 144px; height: 40px; font-size: 9px; }

  /* limits */
  .limits { position: absolute; left: 0; top: 761px; width: 1200px; height: 227px; background: var(--ice); }
  .limits .section-title { top: 44px; font-size: 17.5px; }
  .limits-lede { position: absolute; left: 0; width: 1200px; top: 79px; text-align: center; font-size: 10.3px; line-height: 19px; color: var(--ink); }
  .search-field { position: absolute; left: 421px; top: 146px; width: 251px; height: 31px; background: var(--white); border: 1px solid #dfe3ea; font-size: 9.5px; color: #9a9a9a; line-height: 29px; padding-left: 12px; }
  .btn-search { left: 684px; top: 146px; width: 94px; height: 31px; font-size: 9px; }

  /* footer */
  .site-footer { position: absolute; left: 0; top: 988px; width: 1200px; height: 323px; background: var(--blue); color: var(--white); }
  .site-footer .brand { left: 173px; top: 91px; font-size: 25px; color: var(--white); }
  .social { position: absolute; top: 142px; width: 18px; height: 18px; border-radius: 50%; background: var(--white); }
  .foot-col { position: absolute; top: 62px; }
  .foot-title { font-family: "Poppins", sans-serif; font-weight: 700; font-size: 11.5px; text-transform: uppercase; }
  .foot-rule { width: 20px; height: 1.5px; background: var(--gold); margin-top: 7px; }
  .foot-list { list-style: none; margin-top: 12px; }
  .foot-list li { font-size: 9.6px; line-height: 22.4px; position: relative; padding-left: 11px; }
  .foot-list li::before { content: ""; position: absolute; left: 0; top: 9px; width: 4px; height: 4px; border-radius: 50%; background: var(--white); }
  .foot-about { margin-top: 14px; width: 160px; font-size: 9.6px; line-height: 16px; }
  .to-top { position: absolute; left: 1070px; top: 110px; width: 32px; height: 32px; border-radius: 50%; background: var(--white); display: flex; align-items: center; justify-content: center; }
  .foot-divider { position: absolute; left: 173px; top: 274px; width: 854px; height: 1px; background: rgba(255,255,255,.3); }
  .copyright { position: absolute; left: 0; width: 1200px; top: 292px; text-align: center; font-size: 9px; }
</style>
</head>
<body>
<div class="page">

  <header class="site-header">
    <div class="brand"><span>Homevale</span><span class="brand-mark"></span></div>
    <span class="nav-link" style="left:316px">Rates</span>
    <span class="nav-link" style="left:371px">Purchase</span>
    <span class="nav-link" style="left:446px">Refinace</span>
    <span class="nav-link" style="left:750px;font-weight:400">Schedule a Call</span>
    <span class="nav-link" style="left:848px;font-weight:400">Guides</span>
    <span class="btn btn-apply">Apply Now</span>
  </header>

  <section class="tools">
    <p class="eyebrow">How much can you afford ?</p>
    <h1 class="section-title">Find Out with Our Suite of Mortgage Tools.</h1>

    <div class="tool" style="left:317px;top:156px">
      <svg viewBox="0 0 46 46" fill="none" stroke="#bf0202" stroke-width="1.6" stroke-linejoin="round">
        <path d="M14 18 L28 6 L42 18"/><path d="M18 15 V40 H40 V17"/><rect x="26" y="26" width="7" height="14"/>
        <rect x="3" y="22" width="16" height="22" fill="#edf4ff"/><rect x="6" y="25" width="10" height="5"/>
        <path d="M7 34h2M11 34h2M7 38h2M11 38h2M7 41h2M11 41h2"/>
      </svg>
      <h2 class="tool-name">Mortgage Calculator</h2>
      <p class="tool-desc">See how much you can afford by home price,<br>monthly payment,or income.</p>
    </div>

    <div class="tool" style="left:609px;top:156px">
      <svg viewBox="0 0 46 46" fill="none" stroke="#bf0202" stroke-width="1.6" stroke-linejoin="round">
        <path d="M14 9 L17 3 H27 L30 9 Z"/><path d="M15 10 C4 17 2 42 22 42 C30 42 34 38 34 32"/>
        <circle cx="17" cy="28" r="7"/><path d="M17 23v10M19.5 25.5c-1-1.5-5-1.5-5 .5s5 1.5 5 3.5-4 2-5 .5"/>
        <rect x="27" y="18" width="16" height="24" fill="#edf4ff"/><rect x="30" y="21" width="10" height="5"/>
        <path d="M31 30h2M36 30h2M31 34h2M36 34h2M31 38h2M36 38h2"/>
      </svg>
      <h2 class="tool-name">Refinance Calculator</h2>
      <p class="tool-desc">Should you refinance? This calculator<br>breakdown monthly and lifetime cost.</p>
    </div>

    <div class="tool" style="left:891px;top:156px">
      <svg viewBox="0 0 46 46" fill="none" stroke="#bf0202" stroke-width="1.6" stroke-linejoin="round">
        <rect x="6" y="12" width="26" height="32"/><rect x="10" y="16" width="18" height="6"/>
        <path d="M10 27h4v3h-4zM17 27h4v3h-4zM24 27h4v3h-4zM10 33h4v3h-4zM17 33h4v3h-4zM24 33h4v3h-4zM10 39h4v2h-4zM17 39h4v2h-4zM24 39h4v2h-4z"/>
        <circle cx="34" cy="10" r="8" fill="#edf4ff"/><path d="M34 5v10M36.5 7.5c-1-1.5-5-1.5-5 .5s5 1.5 5 3.5-4 2-5 .5"/>
      </svg>
      <h2 class="tool-name">VA Loan Calculator</h2>
      <p class="tool-desc">Former or current members of the miltary<br>have access to reduced costs and rates</p>
    </div>

    <div class="tool" style="left:317px;top:331px">
      <svg viewBox="0 0 46 46" fill="none" stroke="#bf0202" stroke-width="1.6" stroke-linejoin="round">
        <rect x="3" y="3" width="34" height="40"/><path d="M20 3v40M3 23h17"/>
        <path d="M8 13h8M12 9v8M25 13h8M8 30l7 7M15 30l-7 7"/>
        <circle cx="33" cy="33" r="10" fill="#edf4ff"/><path d="M28 31h10M28 35h10"/>
      </svg>
      <h2 class="tool-name">FHA Calculator</h2>
      <p class="tool-desc">Determine your payment,including FHA-<br>specific mortgage insurance and fees</p>
    </div>

    <div class="tool" style="left:609px;top:331px">
      <svg viewBox="0 0 46 46" fill="none" stroke="#bf0202" stroke-width="1.6" stroke-linejoin="round">
        <path d="M8 32 V4 H32 V14"/><path d="M12 9h14M12 13h10"/>
        <circle cx="20" cy="22" r="6"/><path d="M20 18v8"/>
        <path d="M3 32h14v3H3zM3 35h14v3H3zM3 38h14v4H3z"/>
        <rect x="24" y="18" width="18" height="25" fill="#edf4ff"/><rect x="27" y="21" width="12" height="5"/>
        <path d="M28 30h3M34 30h3M28 34h3M34 34h3M28 38h3M34 38h3"/>
      </svg>
      <h2 class="tool-name">USDA Calculator</h2>
      <p class="tool-desc">The USDA provides a zero-down loan for<br>homes outside major metros.</p>
    </div>

    <div class="tool" style="left:891px;top:331px">
      <svg viewBox="0 0 46 46" fill="none" stroke="#bf0202" stroke-width="1.6" stroke-linejoin="round">
        <circle cx="12" cy="12" r="8"/><path d="M12 7v10M14.5 9.5c-1-1.5-5-1.5-5 .5s5 1.5 5 3.5-4 2-5 .5"/>
        <path d="M6 30 L20 20 L27 24 L42 6"/><path d="M34 6h8v8"/>
        <path d="M3 36h10v8H3zM3 40h10M16 32h10v12H16zM16 36h10M16 40h10M29 28h10v16H29zM29 32h10M29 36h10M29 40h10"/>
      </svg>
      <h2 class="tool-name">USDA Income Limits</h2>
      <p class="tool-desc">Find out if your income level is eligble for<br>this zero-down home loan.</p>
    </div>
  </section>

  <section class="quote" role="img" aria-label="Dimmed aerial photograph of a residential neighbourhood">
    <h2 class="section-title">Get Your Rate Quote Today !</h2>
    <span class="btn btn-purchase">Purchase Rates</span>
    <span class="btn btn-refi">Refinace Rates</span>
  </section>

  <section class="limits">
    <h2 class="section-title">2019 Mortgage Loan Limits For Conventional, FHA, &amp; VA Loans</h2>
    <p class="limits-lede">Mortgage loan limits for every U.S. county, as published by Harbor Mae &amp; Ridge Mac, the Federal<br>Housing Administration (FHA), and the Department of Veterans Affairs (VA)</p>
    <div class="search-field">Please enter the informations...</div>
    <span class="btn btn-search">Search</span>
  </section>

  <footer class="site-footer">
    <div class="brand"><span>Homevale</span><span class="brand-mark" style="background:var(--white)"></span></div>
    <span class="social" style="left:195px"></span>
    <span class="social" style="left:220px"></span>
    <span class="social" style="left:245px"></span>

    <div class="foot-col" style="left:328px">
      <h3 class="foot-title">Links</h3><div class="foot-rule"></div>
      <ul class="foot-list">
        <li>Get a Mortgage Rate Now</li><li>Loan Types</li><li>Homevale Disclosures</li><li>Conforming, VA &amp; FHA Loan Limits</li>
      </ul>
    </div>
    <div class="foot-col" style="left:562px">
      <h3 class="foot-title">Company</h3><div class="foot-rule"></div>
      <ul class="foot-list">
        <li>About Us</li><li>Careers</li><li>Homevale Resources</li><li>Contact</li>
      </ul>
    </div>
    <div class="foot-col" style="left:720px">
      <h3 class="foot-title">Policies</h3><div class="foot-rule"></div>
      <ul class="foot-list">
        <li>Security Policy</li><li>Privacy Policy</li><li>Terms of Use</li><li>Email Policy</li>
      </ul>
    </div>
    <div class="foot-col" style="left:866px">
      <h3 class="foot-title">About Us</h3><div class="foot-rule"></div>
      <p class="foot-about">Lorem ipsum dolor sit amet, consectetur adipiscing elit, sed do eiusmod tempor incididunt ut labore et dolore magna aliqua. Quis ipsum sus-</p>
    </div>

    <span class="to-top">
      <svg width="12" height="12" viewBox="0 0 12 12" fill="none" stroke="#1856a6" stroke-width="1.5" stroke-linecap="round"><path d="M6 10V2M2.5 5.5L6 2l3.5 3.5"/></svg>
    </span>
    <div class="foot-divider"></div>
    <p class="copyright">Copyright © 2009-2019 &nbsp;Homevale, Inc. All rights reserved.</p>
  </footer>

</div>
</body>
</html>
```